Visitenkarten-Design für Commercial Expert
Zielgruppe
Guten Tag! Ich bin Single und suche neue sportliche Bekannte in der Nähe meines Wohnortes.
Aufgabenstellung
Dr. Mareike Venhaus
Commercial Expert
Telefonnummer 01762290471
Anschrift: Tulpenau 9, 72814 Lindenhain
https://www.netzvelo-profil.de/profile/Mareike_Venhaus/

```html
<!DOCTYPE html>
<html lang="de">
<head>
<meta charset="utf-8">
<title>Visitenkarte – Dr. Mareike Venhaus</title>
<link rel="stylesheet" href="https://fonts.googleapis.com/css2?family=Questrial&display=swap">
<style>
  :root {
    --teal: #00757a;
    --teal-dark: #005257;
    --teal-deep: #003a3e;
    --ink: #2b2b2b;
    --paper: #ffffff;
    --backdrop: #e9ecec;
    --back-text: #d4e4e4;
  }
  * { box-sizing: border-box; margin: 0; padding: 0; }
  html, body {
    width: 1200px; height: 900px; overflow: hidden;
    background: var(--backdrop);
    font-family: "Questrial", "Century Gothic", sans-serif;
  }
  .stage { position: relative; width: 1200px; height: 900px; }
  .card {
    position: absolute; left: 250px; width: 700px; height: 400px;
    overflow: hidden; box-shadow: 0 6px 20px rgba(0,0,0,.12);
  }
  .card--front { top: 30px; background: var(--paper); }
  .card--back {
    top: 470px;
    background: radial-gradient(ellipse at 35% 40%, #00898d 0%, var(--teal) 35%, var(--teal-dark) 70%, var(--teal-deep) 100%);
  }

  /* Front */
  .portrait {
    position: absolute; left: 45px; top: 80px; width: 210px; height: 210px;
    border-radius: 50%;
    background: radial-gradient(circle at 50% 40%, #c9a878 0%, #8a7a66 35%, #5a5a5a 70%, #454545 100%);
  }
  .identity { position: absolute; left: 310px; top: 72px; }
  .identity__name {
    color: var(--teal); font-size: 28px; letter-spacing: 2.5px;
    text-transform: uppercase; font-weight: 400; white-space: nowrap;
  }
  .identity__role { color: var(--ink); font-size: 20px; margin-top: 2px; }
  .divider {
    position: absolute; left: 312px; top: 172px; width: 318px; height: 1.5px;
    background: var(--teal);
  }
  .contact { position: absolute; left: 312px; display: flex; align-items: flex-start; gap: 14px; color: var(--ink); font-size: 18px; letter-spacing: 1px; line-height: 1.2; }
  .contact--address { top: 198px; }
  .contact--phone { top: 262px; align-items: center; }
  .contact__icon { width: 20px; height: 20px; flex: none; margin-top: 4px; fill: var(--teal); }
  .contact--phone .contact__icon { margin-top: 0; }
  .contact__lines span { display: block; }

  .strip { position: absolute; background: var(--teal); }
  .strip--left { left: 0; top: 310px; width: 300px; height: 20px; }
  .strip--url {
    left: 426px; top: 306px; width: 274px; height: 24px;
    color: var(--paper); font-size: 11px; letter-spacing: .2px;
    display: flex; align-items: center; padding-left: 8px; white-space: nowrap;
  }
  .network-name {
    position: absolute; left: 312px; top: 310px; height: 20px;
    color: var(--teal); font-size: 14px; letter-spacing: 1px;
    display: flex; align-items: center; gap: 5px;
  }
  .network-name__dot { width: 6px; height: 6px; border-radius: 50%; background: var(--teal); }
  .strip--base { left: 0; top: 345px; width: 700px; height: 24px; }

  /* Back */
  .back-title {
    position: absolute; left: 0; right: 0; top: 150px; text-align: center;
    color: var(--back-text);
  }
  .back-title__name { font-size: 38px; letter-spacing: 4px; text-transform: uppercase; font-weight: 400; }
  .back-title__role { font-size: 26px; margin-top: 4px; letter-spacing: .5px; }
</style>
</head>
<body>
<main class="stage">
  <section class="card card--front" aria-label="Vorderseite">
    <div class="portrait" role="img" aria-label="Porträtfoto von Dr. Mareike Venhaus"></div>

    <div class="identity">
      <h1 class="identity__name">Dr. Mareike Venhaus</h1>
      <p class="identity__role">Commercial Expert</p>
    </div>
    <div class="divider"></div>

    <div class="contact contact--address">
      <svg class="contact__icon" viewBox="0 0 20 20" aria-hidden="true"><path d="M10 2 1 10h3v7h4.5v-5h3v5H16v-7h3z"/></svg>
      <p class="contact__lines"><span>Tulpenau 9, 72814 Lindenhain</span><span>Germany</span></p>
    </div>
    <div class="contact contact--phone">
      <svg class="contact__icon" viewBox="0 0 20 20" aria-hidden="true"><path d="M5.2 1.8 7.6 5.6c.3.5.2 1.1-.2 1.5L6 8.3c.9 2.2 3.5 4.9 5.7 5.8l1.2-1.4c.4-.4 1-.5 1.5-.2l3.8 2.4c.5.3.7 1 .4 1.5l-1.3 2.2c-.4.7-1.2 1-2 .8C8.8 17.8 2.2 11.2.6 4.7.4 3.9.7 3.1 1.4 2.7L3.6 1.4c.5-.3 1.2-.1 1.6.4z"/></svg>
      <p>01762290471</p>
    </div>

    <div class="strip strip--left"></div>
    <p class="network-name"><span>NETZVELO</span><span class="network-name__dot"></span></p>
    <p class="strip strip--url">www.netzvelo-profil.de/profile/Mareike_Venhaus</p>
    <div class="strip strip--base"></div>
  </section>

  <section class="card card--back" aria-label="Rückseite">
    <div class="back-title">
      <h2 class="back-title__name">Dr. Mareike Venhaus</h2>
      <p class="back-title__role">Commercial Expert</p>
    </div>
  </section>
</main>
</body>
</html>
```